ANIMATION BANNER ADS
Lumbra7Vid
I've corrected the consistency font style of
design #47 and I also provided a green version
Hi PH, F.Y.I. If there's any minimal revision on my designs, I will charge it for free :)
Please check my designs, I'm sure you will love it
Design A: #36
Design B: #37
Hello Rashid
will you give some feedback?, let me know what do you think
Dear PH,
You must click the entry and view the full version of the banners so the gif animation will work normally, because it looks weird when viewed in thumbnail.
Thanks
Very good guys, keep it up. 3 days left and there is only one creative winner will win the award. But the creativity never stops here. Show the world your ability guys
Photoshop layer & GIF animation
What file you want sir? Did photoshop layer?

```html
<!DOCTYPE html>
<html lang="en">
<head>
<meta charset="utf-8">
<title>Lumbra7Vid Banner Set</title>
<link rel="stylesheet" href="https://fonts.googleapis.com/css2?family=Open+Sans:wght@600;700;800&display=swap">
<style>
  :root {
    --stage: #000000;
    --green-light: #a6d63a;
    --green-mid: #86c125;
    --green-dark: #5f9d16;
    --purple-light: #8a4aa6;
    --purple-dark: #6b2d88;
    --grey-light: #e9e9e9;
    --grey-dark: #c9c9c9;
    --panel-white: #ffffff;
    --panel-shade: #e3e3e3;
    --logo-grey: #8c8c8c;
    --logo-dot: #8cc63f;
    --headline-white: #ffffff;
    --headline-purple: #7a3a96;
    --button-top: #fff36a;
    --button-bottom: #f2c200;
    --button-text: #3a2a00;
    --product-dark: #2a2a2a;
    --product-mid: #555555;
  }
  * { margin: 0; padding: 0; box-sizing: border-box; }
  html, body { width: 1200px; height: 901px; overflow: hidden; background: var(--stage); }
  body { font-family: "Open Sans", Arial, sans-serif; position: relative; }

  .banner { position: absolute; overflow: hidden; }
  .banner--green { background: linear-gradient(135deg, var(--green-light), var(--green-mid) 55%, var(--green-dark)); }
  .banner--purple { background: linear-gradient(180deg, var(--purple-light), var(--purple-dark)); }
  .banner--grey { background: linear-gradient(180deg, var(--grey-light), var(--grey-dark)); }

  .logo-panel {
    position: absolute; left: 0; top: 0;
    background: linear-gradient(180deg, var(--panel-white), var(--panel-shade));
    display: flex; align-items: center;
  }
  .logo {
    display: flex; align-items: center; gap: 7px;
    font-weight: 700; color: var(--logo-grey); letter-spacing: 0.5px;
  }
  .logo__dot { width: 12px; height: 12px; border-radius: 50%; background: var(--logo-dot); }

  .headline {
    position: absolute; z-index: 2; font-weight: 800; text-transform: uppercase;
    color: var(--headline-white); line-height: 1.2; white-space: nowrap;
  }
  .headline--purple { color: var(--headline-purple); text-align: center; }

  .product {
    position: absolute; z-index: 1; border-radius: 10px;
    background: radial-gradient(circle at 45% 40%, var(--product-mid), var(--product-dark) 70%);
  }

  .join-button {
    position: absolute; z-index: 2; display: flex; align-items: center; justify-content: center;
    border-radius: 5px; font-weight: 800; text-transform: uppercase;
    background: linear-gradient(180deg, var(--button-top), var(--button-bottom));
    color: var(--button-text); box-shadow: 0 2px 3px rgba(0,0,0,0.25);
  }

  /* Leaderboards */
  .leaderboard { left: 258px; width: 913px; }
  .leaderboard .logo-panel { width: 260px; height: 100%; clip-path: polygon(0 0, 100% 0, 82% 100%, 0 100%); padding-left: 22px; }
  .leaderboard .logo { font-size: 21px; }
  .leaderboard .headline { font-size: 23px; }
  .leaderboard .product { left: 642px; top: 12px; width: 96px; height: calc(100% - 20px); }
  .leaderboard .join-button { left: 750px; width: 145px; height: 36px; top: 50%; margin-top: -18px; font-size: 16px; }

  .leaderboard--store { top: 85px; height: 129px; }
  .leaderboard--store .headline { left: 272px; top: 48px; }
  .leaderboard--photo { top: 229px; height: 109px; }
  .leaderboard--photo .headline { left: 308px; top: 38px; }
  .leaderboard--delivery { top: 348px; height: 112px; }
  .leaderboard--delivery .headline { left: 300px; top: 24px; width: 290px; font-size: 22px; }

  /* Skyscraper */
  .skyscraper { left: 32px; top: 83px; width: 204px; height: 752px; }
  .skyscraper .logo-panel { width: 100%; height: 110px; clip-path: polygon(0 0, 100% 0, 100% 62%, 0 100%); padding: 0 0 22px 16px; }
  .skyscraper .logo { font-size: 19px; }
  .skyscraper .headline { left: 0; width: 100%; top: 180px; text-align: center; font-size: 30px; line-height: 1.95; }
  .skyscraper .headline__rank { font-size: 62px; line-height: 1.1; display: block; }
  .skyscraper .product { left: 52px; top: 455px; width: 100px; height: 185px; }
  .skyscraper .join-button { left: 34px; top: 648px; width: 139px; height: 38px; font-size: 16px; }

  /* Medium rectangle */
  .rectangle { left: 258px; top: 484px; width: 377px; height: 351px; }
  .rectangle .logo-panel { width: 320px; height: 90px; clip-path: polygon(0 0, 100% 0, 84% 100%, 0 100%); padding-left: 22px; }
  .rectangle .logo { font-size: 21px; }
  .rectangle .headline { left: 22px; top: 118px; font-size: 24px; line-height: 1.4; }
  .rectangle .product { left: 205px; top: 192px; width: 140px; height: 145px; }
  .rectangle .join-button { left: 24px; top: 218px; width: 138px; height: 36px; font-size: 16px; }
</style>
</head>
<body>

  <section class="banner skyscraper banner--green">
    <div class="logo-panel"><div class="logo"><span class="logo__dot"></span>Lumbra7Vid</div></div>
    <h2 class="headline"><span class="headline__rank">#1</span>Qatar<br>On Line<br>Store</h2>
    <div class="product" role="img" aria-label="Camera flash unit product photo"></div>
    <div class="join-button">Join Now</div>
  </section>

  <section class="banner leaderboard leaderboard--store banner--green">
    <div class="logo-panel"><div class="logo"><span class="logo__dot"></span>Lumbra7Vid</div></div>
    <h2 class="headline">#1 Qatar On Line Store</h2>
    <div class="product" role="img" aria-label="Camera flash unit product photo"></div>
    <div class="join-button">Join Now</div>
  </section>

  <section class="banner leaderboard leaderboard--photo banner--purple">
    <div class="logo-panel"><div class="logo"><span class="logo__dot"></span>Lumbra7Vid</div></div>
    <h2 class="headline">For Photorgapher</h2>
    <div class="product" role="img" aria-label="DSLR camera product photo"></div>
    <div class="join-button">Join Now</div>
  </section>

  <section class="banner leaderboard leaderboard--delivery banner--grey">
    <div class="logo-panel"><div class="logo"><span class="logo__dot"></span>Lumbra7Vid</div></div>
    <h2 class="headline headline--purple">Instant Delvery<br>For Qatar</h2>
    <div class="product" role="img" aria-label="Studio softbox light product photo"></div>
    <div class="join-button">Join Now</div>
  </section>

  <section class="banner rectangle banner--green">
    <div class="logo-panel"><div class="logo"><span class="logo__dot"></span>Lumbra7Vid</div></div>
    <h2 class="headline">#1 Qatar<br>On Line Store</h2>
    <div class="product" role="img" aria-label="Camera flash unit product photo"></div>
    <div class="join-button">Join Now</div>
  </section>

</body>
</html>
```